Chimney Service company needs new business card design

We need a updated business card with our new logo added. We provide a full range of chimney services throughout Vermont and New Hampshire. The business card will be one sided and color. Attached is our current business card another document showing all the information we would like on the card.
We dont like a lot of flashy colors.... here is a link to our website to get an idea of our branding www.flueguardianvt.example

Target Market(s)

homeowners

Industry/Entity Type

Business

Contact Information for Business Card

See attached sheet for content.

Font styles to use
Serif
Sans Serif

Requirements
Must have
• all information provided on separate sheet
Should not have
• Additional information that may clogg up design

```html
<!DOCTYPE html>
<html lang="en">
<head>
<meta charset="utf-8">
<title>Flue Guardian – Business Card</title>
<link rel="stylesheet" href="https://fonts.googleapis.com/css2?family=Cinzel:wght@400;500&family=Lato:wght@400&display=swap">
<style>
  :root {
    --backdrop: #6a6a6a;
    --card-light: #f2f2f2;
    --brand-red: #9b0a0a;
    --brand-red-deep: #8a0404;
    --ink: #2b2b2b;
    --ink-soft: #3a3a3a;
    --white: #ffffff;
  }
  * { margin: 0; padding: 0; box-sizing: border-box; }
  html, body {
    width: 1200px; height: 900px; overflow: hidden;
    background: var(--backdrop);
  }
  .canvas { position: relative; width: 1200px; height: 900px; }
  .card {
    position: absolute; top: 170px; width: 347px; height: 561px;
  }
  .card-front { left: 259px; background: var(--card-light); }
  .card-back {
    left: 631px;
    background: linear-gradient(160deg, var(--brand-red) 0%, var(--brand-red-deep) 60%, #9a0f0f 100%);
  }

  .brand-mark {
    position: absolute; left: 0; width: 100%;
    display: flex; align-items: center; justify-content: center; gap: 10px;
    font-family: 'Cinzel', serif; font-weight: 500; letter-spacing: 1px;
  }
  .brand-mark .mark-square { width: 14px; height: 14px; }
  .card-front .brand-mark { top: 90px; font-size: 24px; color: var(--ink); }
  .card-front .mark-square { background: var(--ink); }
  .card-back .brand-mark { top: 325px; font-size: 30px; color: var(--white); }
  .card-back .mark-square { background: var(--white); width: 18px; height: 18px; }

  .service-band {
    position: absolute; top: 193px; left: 0; width: 100%; height: 64px;
    background: var(--brand-red); color: var(--white);
    font-family: 'Cinzel', serif; font-size: 19.5px; line-height: 23px;
    text-align: center; padding-top: 9px; letter-spacing: 0.4px;
  }

  .credentials {
    position: absolute; top: 271px; width: 100%; text-align: center;
    font-family: 'Lato', sans-serif; font-size: 14.8px; line-height: 23px;
    color: var(--ink); letter-spacing: 0.1px;
  }
  .credentials .divider { color: var(--brand-red); padding: 0 5px; }

  .service-list {
    position: absolute; top: 326px; width: 100%; list-style: none; text-align: center;
    font-family: 'Lato', sans-serif; font-size: 16.8px; line-height: 20px; color: var(--ink-soft);
  }

  .contact-icons {
    position: absolute; top: 445px; left: 0; width: 100%;
    display: flex; align-items: center; justify-content: center; gap: 8px;
  }
  .contact-icons .rule { width: 58px; height: 1px; background: var(--ink); }
  .contact-icons .icon {
    width: 20px; height: 20px; background: var(--brand-red);
    display: flex; align-items: center; justify-content: center;
  }
  .contact-details {
    position: absolute; top: 470px; width: 100%; text-align: center;
    font-family: 'Lato', sans-serif; font-size: 16px; line-height: 20.5px; color: var(--ink);
  }
</style>
</head>
<body>
<main class="canvas">
  <section class="card card-front">
    <div class="brand-mark"><span class="mark-square"></span>Flue Guardian</div>

    <div class="service-band">Serving VT and New<br>Hampshire since 1989</div>

    <div class="credentials">
      <p>FULLY INSURED<span class="divider">|</span>FREE ESTIMATES</p>
      <p>FAMILY OWNED AND OPERATED</p>
    </div>

    <ul class="service-list">
      <li>Full Masonry Services</li>
      <li>Historic chimney restoration</li>
      <li>Stainless steel liners</li>
      <li>New Chimney installations</li>
      <li>Guild Certified Chimney sweeps</li>
    </ul>

    <div class="contact-icons">
      <span class="rule"></span>
      <span class="icon" aria-label="Phone">
        <svg width="11" height="11" viewBox="0 0 24 24"><path fill="#fff" d="M6.6 10.8a15.1 15.1 0 0 0 6.6 6.6l2.2-2.2a1 1 0 0 1 1-.25 11.4 11.4 0 0 0 3.6.57 1 1 0 0 1 1 1V20a1 1 0 0 1-1 1A17 17 0 0 1 3 4a1 1 0 0 1 1-1h3.5a1 1 0 0 1 1 1c0 1.25.2 2.450.57 3.57a1 1 0 0 1-.25 1z"/></svg>
      </span>
      <span class="icon" aria-label="Email">
        <svg width="11" height="9" viewBox="0 0 22 16"><rect x="0" y="0" width="22" height="16" fill="#fff"/><path d="M1 1l10 8 10-8" stroke="#9b0a0a" stroke-width="2" fill="none"/></svg>
      </span>
      <span class="icon" aria-label="Website">
        <svg width="11" height="11" viewBox="0 0 24 24"><circle cx="12" cy="12" r="10" fill="#fff"/><path d="M2 12h20M12 2c3 3 3 17 0 20M12 2c-3 3-3 17 0 20" stroke="#9b0a0a" stroke-width="1.6" fill="none"/></svg>
      </span>
      <span class="rule"></span>
    </div>

    <div class="contact-details">
      <p>802-555-0147</p>
      <p>info@flueguardianvt.example</p>
      <p>www.flueguardianvt.example</p>
    </div>
  </section>

  <section class="card card-back">
    <div class="brand-mark"><span class="mark-square"></span>Flue Guardian</div>
  </section>
</main>
</body>
</html>
```